Plakat-Design für Vereinsfest
Zielgruppe
Unser Verein veranstaltet jedes Jahr im August das Vereinsfest 'Sonnwendtag', das in einem kleinen Wäldchen innerhalb des Heimatortes stattfindet. Am Samstag und Sonntag sorgen verschiedene Musikgruppen für Unterhaltung. Es soll ein Veranstaltungsplakat gestaltet werden, dass sich an die Vorgaben (siehe unten) hält und die Veranstaltung bewirbt.
Zielgruppe sind Bürger des Heimatortes.
Aufgabenstellung
Das Vereinslogo ist beigefügt und sollte prominent auf dem Plakat vertreten sein, Logo und Schriftzug können auch getrennt oder anders angeordnet werden. Der Veranstaltungstitel lautet "Sonnwendtag", es findet am 20. und 21. August "Am Hirtenstein" (Veranstaltungsort) statt.
Programmpunkte: Samstag: Musikalische Unterhaltung mit den Bachpfeifern; Sonntag: Musikalische Unterhaltung mit den Moorbachrabauken
Uhrzeiten sollten enthalten sein:
Beginn Samstag: ab 15 Uhr
Beginn Sonntag: ab 10 Uhr
Das Plakat soll gut leserlich auch aus der Entfernung sein, da es an Straßen plakatiert wird.
Das Plakat soll für spätere Jahre editierbar sein.
Schriftart im Logo: Californian FB Bold (muss aber nicht auf andere Textelemente angewendet werden). Das Plakat soll in DIN A2 gedruckt werden. Die Webadresse sollte auf dem Plakat stehen.

```html
<!DOCTYPE html>
<html lang="de">
<head>
<meta charset="utf-8">
<title>Sonnwendtag – Veranstaltungsplakat</title>
<link rel="stylesheet" href="https://fonts.googleapis.com/css2?family=Bree+Serif&family=Fira+Sans:wght@400;500&display=swap">
<style>
  :root {
    --sage: #c4dfbd;
    --forest: #0f5a2a;
    --festival-red: #ad1716;
    --ink: #1a1a1a;
    --club-blue: #1c2f72;
    --emblem-blue: #b9c9ea;
    --paper: #ffffff;
    --frame: #8c8c8c;
    --hill-light: #9dc98d;
    --hill-mid: #6ea25a;
    --hill-dark: #2c5e2c;
  }
  * { margin: 0; padding: 0; box-sizing: border-box; }
  html, body { width: 848px; height: 1200px; overflow: hidden; background: var(--paper); }
  .poster {
    position: relative;
    width: 848px; height: 1200px;
    background: var(--sage);
    border: 1px solid var(--frame);
    overflow: hidden;
  }
  .headline-block { position: absolute; left: 0; right: 0; text-align: center; font-family: "Bree Serif", Georgia, serif; line-height: 1; }
  .invite { top: 42px; font-size: 40px; color: var(--forest); }
  .event-title { top: 100px; font-size: 124px; color: var(--festival-red); white-space: nowrap; }
  .event-date { top: 268px; font-size: 66px; color: var(--forest); }
  .event-venue { top: 340px; font-size: 66px; color: var(--forest); white-space: nowrap; }

  .programme { position: absolute; top: 437px; width: 390px; text-align: center; }
  .programme--saturday { left: 27px; }
  .programme--sunday { left: 431px; }
  .programme__day { font-family: "Bree Serif", Georgia, serif; font-size: 31px; color: var(--forest); line-height: 1.2; }
  .programme__act { font-family: "Fira Sans", Arial, sans-serif; font-size: 21.5px; line-height: 1.45; color: var(--ink); margin-top: 4px; letter-spacing: 0.3px; }

  .landscape {
    position: absolute; left: 0; top: 600px; width: 848px; height: 288px;
    background: linear-gradient(180deg, var(--sage) 0%, var(--hill-light) 25%, var(--hill-mid) 60%, var(--hill-dark) 100%);
  }

  .web-band {
    position: absolute; left: 0; top: 887px; width: 848px; height: 52px;
    background: var(--festival-red);
    color: var(--paper);
    font-family: "Fira Sans", Arial, sans-serif; font-size: 28px; letter-spacing: 1px;
    display: flex; align-items: center; justify-content: center;
  }

  .club-footer { position: absolute; left: 0; top: 939px; width: 848px; height: 261px; background: var(--paper); }
  .club-emblem { position: absolute; left: 106px; top: 28px; width: 206px; height: 206px; border-radius: 50%; background: var(--emblem-blue); }
  .club-name {
    position: absolute; left: 335px; top: 44px;
    font-family: "Bree Serif", Georgia, serif; color: var(--club-blue);
    line-height: 1;
  }
  .club-name__small { font-size: 24px; display: block; margin-left: 64px; }
  .club-name__large { font-size: 48px; display: block; margin-top: 3px; white-space: nowrap; }
  .club-name__large--indent { margin-left: 34px; }
</style>
</head>
<body>
<main class="poster">
  <p class="headline-block invite">Wir laden ein zum:</p>
  <h1 class="headline-block event-title">Sonnwendtag</h1>
  <p class="headline-block event-date">20. und 21. August</p>
  <p class="headline-block event-venue">„Am Hirtenstein“</p>

  <section class="programme programme--saturday">
    <h2 class="programme__day">Samstag ab 15 Uhr:</h2>
    <p class="programme__act">Musikalische Unterhaltung mit<br>den Bachpfeifern</p>
  </section>
  <section class="programme programme--sunday">
    <h2 class="programme__day">Sonntag ab 10 Uhr:</h2>
    <p class="programme__act">Musikalische Unterhaltung mit<br>den Moorbachrabauken</p>
  </section>

  <div class="landscape" role="img" aria-label="Illustrierte Waldlandschaft mit Nadelbäumen und grünen Hügeln"></div>

  <div class="web-band">www.heimatverein-lindenau.de</div>

  <footer class="club-footer">
    <div class="club-emblem" aria-hidden="true"></div>
    <p class="club-name">
      <span class="club-name__small">Historischer</span>
      <span class="club-name__large">Heimat- und</span>
      <span class="club-name__large club-name__large--indent">Trachtenverein</span>
      <span class="club-name__large">Lindenau e.V.</span>
    </p>
  </footer>
</main>
</body>
</html>
```